Humorous Book by Comedian Needs E-book Cover

My book 'A Kettle on the Porch' is on Leafpad but I want a better cover designed. Cover needs my photo on it. My name is the most important text (because I have an existing audience.)

Text elements:
Author: Dorvel Pim
Title: A Kettle on the Porch
Subtitle: Tenth Anniversary Edition
Review Quote: 'All of his columns are amusing. The best are masterpieces.' Harbour Ledger

Above my name it should say: Collected Humour From NZ's Award-Winning Comedian

Here's the present version (which is why I want an improved version!)
http://www.brightmart-example.com/A-Kettle-Porch-Anniversary-Edition-ebook/dp/Q77TX2M904

Book covers I admire:

http://www.brightmart-example.co.uk/Why-The-Fern-Odile-Brask-ebook/dp/Q3318ZR7LN/ref=tmm_kin_title_0

http://www.brightmart-example.com/Gravelhat-Mira-Dunst-ebook/dp/Q691PLE583/ref=tmm_kin_title_0

http://www.brightmart-example.co.uk/Why-Keep-Lantern-Rex-Palfrey-ebook/dp/Q58JN3TQ7V

Leafpad covers need to work as thumbnails, as well as on small device screens.

This cover is for Brightmart Leafpad. Tech specs are on Leafpad Direct Publishing page. Dimensions: Requirements for the size of your cover art have an ideal height/width ratio of 1.6, this means: • A minimum of 625 pixels on the shortest side and 1000 pixels on the longest side • For best quality, your image would be 2820 pixels on the shortest side and 4500 pixels on the longest side

Dimensions Requirements for the size of your cover art have an ideal height/width ratio of 1.6, this means: • A minimum of 625 pixels on the shortest side and 1000 pixels on the longest side • For best quality, your image would be 2820 pixels on the shortest side and 4500 pixels on the longest side

Comedian

```html
<!DOCTYPE html>
<html lang="en">
<head>
<meta charset="utf-8">
<title>A Kettle on the Porch – Dorvel Pim</title>
<link rel="stylesheet" href="https://fonts.googleapis.com/css2?family=Cinzel+Decorative:wght@700&family=Cinzel:wght@400;700&family=Open+Sans:ital,wght@0,700;1,600&family=Playfair+Display:wght@700&family=Marcellus&display=swap">
<style>
  :root {
    --bg-top: #86878a;
    --bg-bottom: #d4d4d5;
    --navy: #0f3a78;
    --cream: #ece7cf;
    --cream-shade: #b9b39a;
    --wine: #6e1f33;
    --photo-dark: #3e3733;
    --photo-skin: #b98d6d;
    --photo-jacket: #ebe5cc;
  }
  html, body { margin: 0; padding: 0; overflow: hidden; }
  body { width: 752px; height: 1200px; }
  .cover {
    position: relative;
    width: 752px;
    height: 1200px;
    overflow: hidden;
    background: linear-gradient(180deg, var(--bg-top) 0%, #a9aaac 45%, var(--bg-bottom) 100%);
    font-family: "Open Sans", Arial, sans-serif;
  }
  .tagline {
    position: absolute; top: 30px; left: 0; width: 100%;
    text-align: center; margin: 0;
    font-weight: 700; font-size: 19.5px; color: var(--navy);
    letter-spacing: 0.2px;
  }
  .title { margin: 0; }
  .title-lead {
    position: absolute; top: 64px; left: 64px;
    font-family: "Cinzel", serif; font-size: 30px; color: var(--cream);
    letter-spacing: 2px;
  }
  .title-main {
    position: absolute; top: 58px; left: 140px; width: 470px;
    text-align: center;
    font-family: "Cinzel Decorative", serif; font-weight: 700;
    font-size: 112px; line-height: 1; color: var(--cream);
    transform: scaleY(1.65); transform-origin: top center;
    text-shadow: 2px 2px 0 var(--cream-shade), 3px 4px 6px rgba(0,0,0,.25);
  }
  .title-tail {
    position: absolute; top: 254px; left: 0; width: 100%;
    text-align: center;
    font-family: "Marcellus", serif; font-size: 40px; line-height: 44px; color: var(--wine);
    letter-spacing: 3px;
  }
  .author-photo {
    position: absolute; left: 0; top: 0; width: 752px; height: 1200px;
  }
  .edition {
    position: absolute; top: 436px; left: 56px; width: 176px;
    text-align: center; color: var(--navy);
  }
  .edition-number {
    font-family: "Playfair Display", serif; font-weight: 700;
    font-variant-numeric: lining-nums;
    font-size: 74px; line-height: 1; color: var(--cream);
    text-shadow: 1px 2px 0 var(--cream-shade);
  }
  .edition-label { font-weight: 700; font-size: 19px; line-height: 1.25; margin-top: 8px; }
  .review {
    position: absolute; top: 566px; right: 30px; width: 300px;
    margin: 0; text-align: right;
    font-style: italic; font-weight: 600; font-size: 16px; line-height: 1.35;
    color: var(--navy);
  }
  .author {
    position: absolute; bottom: 38px; left: 0; width: 100%;
    text-align: center; margin: 0;
    font-family: "Cinzel", serif; font-weight: 700; font-size: 80px; color: var(--navy);
    letter-spacing: 6px; line-height: 1;
  }
</style>
</head>
<body>
<main class="cover">
  <svg class="author-photo" viewBox="0 0 752 1200" role="img" aria-label="Portrait photo of the author smiling, wearing glasses, a cream dinner jacket and a dark bow tie">
    <defs>
      <linearGradient id="portrait-tone" x1="0" y1="0" x2="0" y2="1">
        <stop offset="0" stop-color="var(--photo-dark)"/>
        <stop offset="0.1" stop-color="var(--photo-dark)"/>
        <stop offset="0.16" stop-color="var(--photo-skin)"/>
        <stop offset="0.33" stop-color="var(--photo-skin)"/>
        <stop offset="0.38" stop-color="var(--photo-jacket)"/>
        <stop offset="1" stop-color="var(--photo-jacket)"/>
      </linearGradient>
    </defs>
    <path d="M262 370 Q280 310 385 310 Q490 312 505 375 L500 490 Q470 545 450 565
             Q560 595 660 645 Q700 705 705 800 L710 1200 L80 1200 L78 800
             Q85 685 120 635 Q220 590 300 565 Q272 525 265 480 Z"
          fill="url(#portrait-tone)"/>
  </svg>

  <p class="tagline">COLLECTED HUMOUR from NZ’s AWARD WINNING COMEDIAN</p>

  <h1 class="title">
    <span class="title-lead">A</span>
    <span class="title-main">KETTLE</span>
    <span class="title-tail">ON THE PORCH</span>
  </h1>

  <div class="edition">
    <div class="edition-number">10th</div>
    <div class="edition-label">ANNIVERSARY<br>EDITION</div>
  </div>

  <p class="review">‘All of his columns are amusing.<br>The best are masterpieces’<br>...Harbour Ledger</p>

  <p class="author">DORVEL PIM</p>
</main>
</body>
</html>
```